Company/Customer - Leave-Behind Card

Need a Standard size post card 4x6
Hard Stock Paper, Glossy
This will be a logo embossed card that is left behind with our customers
after work is completed, and also for potential customers with additional needs
You completed our Company design, for us,
We are Tandry Pane Studio LLC
I will upload logos and some info we need to have on th eproject
Target Market(s)
We are a professional company (Husband, Wife Team) specializing in Installation of premium Window fashions. Drapery, Shades, Blinds and custom window treatments.
We also specialize in project planning, Consultation, take down, put up services and will also provide some designing but are not specialists in the field. We can also take care of installing/hanging other items, such as Mirrors, paintings, etc...
We want to target both current customers, and potential customers for which leads will be generated
Industry/Entity Type
Professional Service
Font styles to use
Colors
Designer to choose colors to be used in the design.
Requirements
Must have
- Our company logo, our partner logos but not as prominent, our skill sets and certifications. Mission statement
Nice to have
- Eye catching colors, simple design, not to busy, or have to much to look at.
- I would like to see the logos embossed or maybe a looking glass effect.
Should not have
- Too busy, or too much to look at

```html
<!DOCTYPE html>
<html lang="en">
<head>
<meta charset="utf-8">
<title>Tandry Pane Studio – Leave-Behind Postcard</title>
<link href="https://fonts.googleapis.com/css2?family=Open+Sans:ital,wght@0,400;0,600;0,700;1,400&family=Lora:ital@1&display=swap" rel="stylesheet">
<style>
  :root{
    --navy:#26346f;
    --navy-deep:#1c2758;
    --sky-soft:#eef3f9;
    --ink:#5e6066;
    --ink-soft:#8a8d93;
    --paper:#ffffff;
    --backdrop:#e7e8ea;
    --rule:#b9bcc2;
  }
  *{box-sizing:border-box;margin:0;padding:0}
  html,body{width:900px;height:1200px;overflow:hidden}
  body{background:var(--backdrop);font-family:"Open Sans",sans-serif;color:var(--ink);position:relative}

  .card{position:absolute;left:40px;width:820px;height:547px;background:var(--paper);overflow:hidden;box-shadow:0 2px 10px rgba(0,0,0,.12)}
  .card--front{top:38px;background:linear-gradient(180deg,var(--sky-soft) 0%,var(--paper) 60%)}
  .card--back{top:618px}

  /* brand lockup */
  .brand{display:flex;align-items:center;gap:10px}
  .brand__mark{width:26px;height:26px;background:var(--navy);flex:none}
  .brand__name{font-weight:700;color:var(--navy);font-size:26px;letter-spacing:.3px;line-height:1;white-space:nowrap}
  .brand__tagline{font-family:"Lora",serif;font-style:italic;color:var(--ink);font-size:10.5px;margin-top:8px}

  /* front */
  .front__brand{position:absolute;left:40px;top:76px;width:320px}
  .front__photo{position:absolute;left:385px;top:0;width:435px;height:322px;background:linear-gradient(135deg,#f4f6f9 0%,#cfd9e6 45%,#3e5796 80%,#2c3f7a 100%)}
  .front__mission-text{position:absolute;left:545px;top:232px;width:255px;color:#fff;font-size:10.5px;line-height:1.45;text-align:right}
  .front__gallery{position:absolute;left:40px;top:222px;display:flex;gap:8px}
  .front__thumb{width:104px;height:84px;background:linear-gradient(160deg,#e8ecf1 0%,#b9c6d6 60%,#8d9cb0 100%);border:2px solid var(--paper)}
  .front__band{position:absolute;left:0;top:322px;width:820px;height:66px}
  .front__band-title{position:absolute;right:28px;top:336px;color:#fff;font-size:27px;font-weight:600}
  .partners{position:absolute;left:0;top:400px;width:820px;height:100px;display:flex;align-items:center;justify-content:space-between;padding:0 24px}
  .partner-badge{display:flex;align-items:center;gap:5px}
  .partner-badge__shape{width:22px;height:22px;border-radius:50%;background:#6b7f9c}
  .partner-badge__bar{width:40px;height:9px;background:#c6ccd5}
  .partner-name{font-weight:700;color:var(--ink);font-size:13px;white-space:nowrap}
  .partner-name--lead{font-size:16px;color:var(--navy-deep)}
  .partners__seals{display:flex;gap:6px}
  .seal{width:28px;height:28px;border:2px solid var(--rule)}
  .seal--round{border-radius:50%}
  .front__foot{position:absolute;left:0;bottom:0;width:820px;height:22px;background:var(--navy)}

  /* back */
  .back__info{position:absolute;left:34px;top:30px;width:380px}
  .heading{color:var(--navy);font-weight:700;font-size:22px;margin-bottom:8px}
  .body-copy{font-size:10.5px;line-height:1.5;margin-bottom:18px}
  .services{list-style:none;font-size:10.5px;line-height:1.65;margin-bottom:20px}
  .services li{display:flex;align-items:center;gap:8px}
  .services li::before{content:"";width:6px;height:6px;background:var(--navy);flex:none}
  .call{color:var(--navy);font-weight:700;font-size:23px}
  .call__sub{font-size:9.5px;color:var(--ink-soft);margin-bottom:26px}
  .back__brand .brand__mark{width:22px;height:22px}
  .back__brand .brand__name{font-size:21px}
  .back__brand .brand__tagline{font-size:9.5px;margin-top:5px}
  .contact{margin-top:14px;font-size:9.5px;line-height:1.55;font-style:normal}
  .back__divider{position:absolute;left:452px;top:34px;width:1px;height:480px;background:var(--rule)}
  .stamp{position:absolute;right:36px;top:34px;width:74px;height:88px;border:2px solid var(--rule)}
  .address-line{position:absolute;left:490px;width:290px;height:1px;background:var(--rule)}
</style>
</head>
<body>

<section class="card card--front" aria-label="Postcard front">
  <div class="front__brand">
    <div class="brand">
      <span class="brand__mark"></span>
      <span class="brand__name">Tandry Pane Studio</span>
    </div>
    <p class="brand__tagline">Professional Installation Of Hard And Soft Window Treatments</p>
  </div>

  <div class="front__photo" role="img" aria-label="Photo of a smiling installer in a blue work shirt beside a bright window"></div>
  <p class="front__mission-text">We install premium drapery, shades and blinds with care, precision and respect for your home. Every project is planned with you, finished cleanly and left looking exactly the way you pictured it.</p>

  <div class="front__gallery">
    <div class="front__thumb" role="img" aria-label="Photo of a living room with roman shades"></div>
    <div class="front__thumb" role="img" aria-label="Photo of tall windows with sheer shades"></div>
    <div class="front__thumb" role="img" aria-label="Photo of a bright room with fitted blinds"></div>
  </div>

  <svg class="front__band" viewBox="0 0 820 66" preserveAspectRatio="none" aria-hidden="true">
    <path d="M0 50 C180 50 300 0 430 0 L820 0 L820 66 L0 66 Z" fill="var(--navy)"/>
    <path d="M0 44 C180 44 300 -6 430 -6" fill="none" stroke="#9fb1cf" stroke-width="2"/>
  </svg>
  <h2 class="front__band-title">Our Mission</h2>

  <div class="partners">
    <div class="partner-badge"><span class="partner-badge__shape"></span><span class="partner-badge__bar"></span></div>
    <div class="partner-badge"><span class="partner-badge__shape"></span><span class="partner-badge__bar"></span></div>
    <span class="partner-name">Halbrook</span>
    <span class="partner-name partner-name--lead">Larkmoor Shades</span>
    <span class="partner-name">Velden Blinds</span>
    <span class="partner-name">Ostra</span>
    <span class="partner-name">Corvel</span>
    <div class="partners__seals">
      <span class="seal seal--round"></span>
      <span class="seal"></span>
    </div>
  </div>
  <div class="front__foot"></div>
</section>

<section class="card card--back" aria-label="Postcard back">
  <div class="back__info">
    <h2 class="heading">About Us</h2>
    <p class="body-copy">Tandry Pane Studio is a husband and wife team installing drapery, shades, blinds and custom treatments. We also handle planning, consultation, take down and put up services, and hang mirrors and art with the same care.</p>

    <h2 class="heading">Our Services</h2>
    <ul class="services">
      <li>Drapery and soft treatment installs</li>
      <li>Shades and blinds fitted to measure</li>
      <li>Project planning and consultation</li>
      <li>Take down and put up services</li>
      <li>Mirrors, paintings and wall hangings</li>
    </ul>

    <p class="call">Call us on - 00 000 0000</p>
    <p class="call__sub">For Further Information</p>

    <div class="back__brand">
      <div class="brand">
        <span class="brand__mark"></span>
        <span class="brand__name">Tandry Pane Studio</span>
      </div>
      <p class="brand__tagline">Professional Installation Of Hard And Soft Window Treatments</p>
    </div>

    <address class="contact">
      Address: 14 Harlow Road, Suite 2<br>
      Brookfield Heights, OH 44000<br>
      Phone: 000 000 0000 &nbsp; Fax: 000 000 0000<br>
      Email: hello@tandrypanestudio.com
    </address>
  </div>

  <div class="back__divider"></div>
  <div class="stamp"></div>
  <div class="address-line" style="top:268px"></div>
  <div class="address-line" style="top:312px"></div>
  <div class="address-line" style="top:356px"></div>
  <div class="address-line" style="top:400px"></div>
</section>

</body>
</html>
```